Business Card Design

My company is a Consulting & Training company (Halvorn Consulting and Training, LLC) specializing in Firearms Training, State of Florida Concealed Weapons Permit Course, and Tactical Equipment Consulting.

Industry/Entity Type

Business

Contact Information for Business Card

Tobin Halvorn
P.O. Box 412763
Aventura, FL 33197
(786)555-0148

```html
<!DOCTYPE html>
<html lang="en">
<head>
<meta charset="utf-8">
<title>Halvorn Consulting and Training — Business Card</title>
<link href="https://fonts.googleapis.com/css2?family=Roboto+Condensed:wght@400;700&display=swap" rel="stylesheet">
<style>
  :root {
    --ink: #0b0b0b;
    --paper: #f4f4f4;
    --paper-edge: #d9d9d9;
    --stage: #e9e6e1;
    --white: #ffffff;
    --rule: #8a8a8a;
    --photo-light: #e8e6e3;
    --photo-dark: #6e6a66;
  }
  html, body {
    margin: 0;
    width: 1200px;
    height: 902px;
    overflow: hidden;
    background: var(--stage);
  }
  .stage {
    position: relative;
    width: 1200px;
    height: 902px;
  }
  .card {
    position: absolute;
    left: 250px;
    width: 700px;
    height: 400px;
    border-radius: 22px;
    overflow: hidden;
    box-shadow: 0 6px 18px rgba(0,0,0,0.18);
    background: var(--paper);
  }
  .card--front { top: 38px; }
  .card--back  { top: 464px; }
  .card svg { display: block; }
  .type {
    font-family: "Roboto Condensed", "Arial Narrow", sans-serif;
  }
  .title { font-weight: 700; font-size: 40px; }
  .title--light { fill: var(--white); }
  .title--dark { fill: var(--ink); }
  .address { fill: var(--white); font-size: 19px; }
  .holder-name { fill: var(--white); font-size: 32px; }
  .contact { fill: var(--white); font-size: 19px; }
  .service-head { fill: var(--ink); font-size: 20px; font-weight: 700; }
  .service-item { fill: var(--ink); font-size: 18px; }
</style>
</head>
<body>
<main class="stage">

  <!-- Front side -->
  <section class="card card--front" aria-label="Card front">
    <svg width="700" height="400" viewBox="0 0 700 400">
      <defs>
        <linearGradient id="photoTone" x1="0" y1="0" x2="1" y2="1">
          <stop offset="0" stop-color="var(--photo-light)"/>
          <stop offset="1" stop-color="var(--photo-dark)"/>
        </linearGradient>
        <linearGradient id="photoToneAlt" x1="0" y1="0" x2="1" y2="1">
          <stop offset="0" stop-color="#f3f2f0"/>
          <stop offset="1" stop-color="#8c8780"/>
        </linearGradient>
      </defs>
      <rect class="band band--top" x="0" y="0" width="700" height="88" fill="var(--ink)"/>
      <rect class="panel" x="0" y="88" width="700" height="232" fill="var(--paper)"/>
      <rect class="band band--bottom" x="0" y="320" width="700" height="80" fill="var(--ink)"/>

      <text class="type title title--light" x="36" y="62">Halvorn Consulting and Training, LLC</text>

      <rect class="photo-frame" x="58" y="104" width="280" height="202" fill="none" stroke="var(--ink)" stroke-width="5"/>
      <rect class="photo" x="64" y="110" width="268" height="190" fill="url(#photoTone)"
            role="img" aria-label="Photo of a handgun resting on a shooting target"/>

      <rect class="photo-frame" x="372" y="104" width="272" height="202" fill="none" stroke="var(--ink)" stroke-width="5"/>
      <rect class="photo" x="378" y="110" width="260" height="190" fill="url(#photoToneAlt)"
            role="img" aria-label="Photo of a pistol, a revolver and loose cartridges"/>

      <text class="type address" x="664" y="366" text-anchor="end">P.O. Box 412763 Aventura, FL 33197</text>
    </svg>
  </section>

  <!-- Back side -->
  <section class="card card--back" aria-label="Card back">
    <svg width="700" height="400" viewBox="0 0 700 400">
      <rect class="panel" x="0" y="0" width="700" height="400" fill="var(--paper)"/>

      <text class="type title title--dark" x="36" y="72">Halvorn Consulting and Training, LLC</text>

      <polygon class="band" points="0,192 300,192 340,100 700,100 700,214 420,214 382,300 0,300" fill="var(--ink)"/>
      <line class="divider" x1="372" y1="112" x2="332" y2="205" stroke="var(--rule)" stroke-width="1.5"/>

      <text class="type holder-name" x="48" y="258">Tobin Halvorn</text>

      <g class="contact-list">
        <g class="contact-icon" transform="translate(398,122)">
          <rect width="20" height="20" rx="4" fill="var(--white)"/>
          <path d="M6 4 l3 0 l1 4 l-2 1.5 q1.5 3 4 4.5 l1.5 -2 l4 1 l0 3 q-8 0 -12 -8 z" fill="var(--ink)" transform="scale(0.85) translate(1,1)"/>
        </g>
        <text class="type contact" x="428" y="139">(786)555-0148</text>

        <g class="contact-icon" transform="translate(398,152)">
          <rect width="20" height="20" rx="4" fill="var(--white)"/>
          <rect x="4" y="6" width="12" height="9" fill="none" stroke="var(--ink)" stroke-width="1.6"/>
          <polyline points="4,6 10,11 16,6" fill="none" stroke="var(--ink)" stroke-width="1.6"/>
        </g>
        <text class="type contact" x="428" y="169">HalvornCT@Fieldmail.com</text>

        <g class="contact-icon" transform="translate(398,182)">
          <rect width="20" height="20" rx="4" fill="var(--white)"/>
          <path d="M10 17 q-5 -6 -5 -9 a5 5 0 0 1 10 0 q0 3 -5 9 z" fill="var(--ink)"/>
          <circle cx="10" cy="8" r="1.8" fill="var(--white)"/>
        </g>
        <text class="type contact" x="428" y="199">P.O. Box 412763 Aventura, FL 33197</text>
      </g>

      <g class="services" text-anchor="middle">
        <text class="type service-head" x="512" y="248">Service</text>
        <text class="type service-item" x="512" y="276">Firearms Training</text>
        <text class="type service-item" x="512" y="300">Tactical Equipment Consulting</text>
        <text class="type service-item" x="512" y="324">State of Florida Concealed Weapons Permit Course</text>
      </g>
    </svg>
  </section>

</main>
</body>
</html>
```